Flyer Design Project

We need a flyer design for a 1 year old domestic cleaning company based in Wiltshire, England. We provide households with high quality, hard working cleaners. We would like to see designs which use blue (the colour on the logo attatched). The final design should communicate a clean, premier and thorough service in a clear and bold way. We would like the flyer to be A5 with a single sided design. We have attached an A5 word document with the words we would like to be used in the design, what we need is for you to give it some life, colour, artwork and a professional touch. We are perfectionsists which we would like to illustrate to our customer through this flyer.
Updates

payment has been guaranteed!

Sorry..... please no pictures of females on the designs. many thanks

Target Market(s)

females with higher than average income, aged 30-50. Have families and work 9-5.

Industry/Entity Type

It Company

Requirements
Must have
• The flyer must include the logo attatched and the words in the A5 document attatched. With RELIABLE CLEANERS preferably the headline. A5 - single sided.
The Flyer must also include our introductory offer.....
First Clean FREE
Allow us to demonstrate our standards

this should be emphasised.

PLEASE NOTE: can this be added to the list of words on the flyer please:

Ironing service - one day turn around
Nice to have
• some pictures - nothing cheesey. Again, pictures should communicate our modern professional approach.

```html
<!DOCTYPE html>
<html lang="en">
<head>
<meta charset="utf-8">
<title>Brookmere Cleaners – Flyer</title>
<link rel="stylesheet" href="https://fonts.googleapis.com/css2?family=Archivo+Black&family=Arimo:ital,wght@1,700&family=Carlito&family=Poppins:wght@600&family=Open+Sans:wght@700&display=swap">
<style>
  :root {
    --brand-blue: #2260ab;
    --deep-blue: #1d57a0;
    --sun-yellow: #ffe100;
    --ink: #151515;
    --paper: #ffffff;
  }
  * { box-sizing: border-box; margin: 0; padding: 0; }
  html, body { width: 846px; height: 1200px; overflow: hidden; background: var(--paper); }
  .flyer { position: relative; width: 846px; height: 1200px; overflow: hidden; background: var(--brand-blue); }
  .flyer__backdrop { position: absolute; inset: 0; }
  .headline {
    position: absolute; top: 26px; left: 0; width: 846px; text-align: center;
    font-family: "Archivo Black", "Arial Black", sans-serif; font-size: 74px; line-height: 1;
    color: var(--brand-blue); letter-spacing: -0.5px;
  }
  .brand { position: absolute; left: 232px; top: 300px; }
  .brand__name {
    font-family: "Carlito", "Calibri", sans-serif; font-size: 50px; line-height: 1;
    color: var(--ink); display: flex; align-items: center; gap: 14px;
  }
  .brand__dot { width: 44px; height: 44px; border-radius: 50%; background: var(--brand-blue); flex: none; }
  .brand__tagline {
    margin: 8px 0 0 88px; font-family: "Carlito", "Calibri", sans-serif; font-size: 23px; color: var(--ink);
  }
  .offer {
    position: absolute; left: 418px; top: 418px;
    font-family: "Arimo", Arial, sans-serif; font-style: italic; font-weight: 700; font-size: 44px;
    color: var(--ink); text-shadow: 2px 3px 3px rgba(0,0,0,.35);
  }
  .offer__free { color: var(--brand-blue); font-size: 50px; }
  .invite { position: absolute; left: 122px; top: 580px; font-family: "Poppins", sans-serif; font-weight: 600; font-size: 31px; line-height: 48px; }
  .invite__lead { color: var(--paper); }
  .invite__follow { color: var(--ink); padding-left: 133px; }
  .standards { position: absolute; right: 290px; top: 700px; list-style: none; }
  .standards__item {
    display: flex; justify-content: flex-end; align-items: center; gap: 22px; height: 48px;
    font-family: "Carlito", "Calibri", sans-serif; font-size: 32px; color: var(--sun-yellow);
  }
  .standards__mark { width: 28px; height: 28px; border-radius: 50%; background: var(--paper); flex: none; }
  .gallery { position: absolute; left: 645px; top: 642px; width: 152px; display: flex; flex-direction: column; }
  .gallery__photo { height: 122px; }
  .gallery__photo--bedroom { background: linear-gradient(180deg, #9eb6d2, #e7e4df 55%, #c8bfb2); }
  .gallery__photo--lounge { background: linear-gradient(180deg, #cfd8e2, #d9c8ad 55%, #8a7d6e); }
  .gallery__photo--bathroom { background: linear-gradient(180deg, #8a8278, #ddd6cc 50%, #6f5a48); }
  .contact { position: absolute; left: 376px; top: 1070px; font-family: "Open Sans", Arial, sans-serif; font-weight: 700; font-size: 19.5px; line-height: 30px; color: var(--paper); }
  .contact__label { color: var(--sun-yellow); }
</style>
</head>
<body>
<main class="flyer">
  <svg class="flyer__backdrop" width="846" height="1200" viewBox="0 0 846 1200" aria-hidden="true">
    <path d="M0 0 H846 V118 C600 122 330 170 0 260 Z" fill="var(--sun-yellow)"/>
    <path d="M230 268 C420 190 640 150 846 140" fill="none" stroke="var(--deep-blue)" stroke-width="14"/>
    <path d="M150 330 C350 215 610 170 846 160 L846 470 C700 512 520 540 370 545 C260 530 170 440 150 330 Z" fill="var(--paper)"/>
    <path d="M220 290 C410 205 640 170 846 160" fill="none" stroke="var(--ink)" stroke-width="18"/>
    <path d="M420 540 C600 528 740 500 846 472" fill="none" stroke="var(--ink)" stroke-width="16"/>
    <path d="M440 556 C620 545 750 520 846 494" fill="none" stroke="var(--paper)" stroke-width="4"/>
  </svg>

  <h1 class="headline">Reliable Cleaners!</h1>

  <div class="brand">
    <p class="brand__name"><span class="brand__dot"></span>Brookmere Cleaners</p>
    <p class="brand__tagline">Premier Domestic Cleaners</p>
  </div>

  <p class="offer">First Clean <span class="offer__free">FREE</span></p>

  <p class="invite">
    <span class="invite__lead">Allow us to demonstrate</span><br>
    <span class="invite__follow">our standards...</span>
  </p>

  <ul class="standards">
    <li class="standards__item">Personalised service <span class="standards__mark"></span></li>
    <li class="standards__item">Constantly thorough <span class="standards__mark"></span></li>
    <li class="standards__item">Hassel free <span class="standards__mark"></span></li>
    <li class="standards__item">Insured <span class="standards__mark"></span></li>
    <li class="standards__item">Regular weekly cleans <span class="standards__mark"></span></li>
    <li class="standards__item">No contracts <span class="standards__mark"></span></li>
  </ul>

  <div class="gallery">
    <div class="gallery__photo gallery__photo--bedroom" role="img" aria-label="Photo of a bright, tidy bedroom with a chandelier"></div>
    <div class="gallery__photo gallery__photo--lounge" role="img" aria-label="Photo of a clean living room with sofas and bay window"></div>
    <div class="gallery__photo gallery__photo--bathroom" role="img" aria-label="Photo of a spotless bathroom with basin and rug"></div>
  </div>

  <p class="contact">
    <span class="contact__label">Tele:</span> 07700900461<br>
    <span class="contact__label">Email:</span> brookmerecleaners@example.co.uk
  </p>
</main>
</body>
</html>
```